Plume & Crest Hair Extensions needs a business card

We need a business card designed for an online luxury hair extensions business called Plume & Crest, we already have a logo and need an innovative business card (2-sided preferably). The strap line for the brand is 'Luxury Hair At Every Touchpoint!'. The brand is a premium brand selling virgin hair extensions and the target market is the mid-affluent ethnic woman as such the design should reflect this. The brand logo is grey and can be sent when requested.

Target Market(s)

25 to 35 year mid-affluent ethnic woman (Afro-American, Mixed Race, Asian)

Industry/Entity Type

Hair

Colors

Designer to choose colors to be used in the design.

Requirements
Must have
• Business Name: Plume and Crest
Strapline: Luxury hair at every touchpoint!
Domain: ​www.plumeandcrest.example
Email: info@plumeandcrest.example
sales and enquiries
44 07500 xxxxxxx

Please use the grey main brand logo depicted in page 2 of the attached pdf document

```html
<!DOCTYPE html>
<html lang="en">
<head>
<meta charset="utf-8">
<title>Plume &amp; Crest – Business Card</title>
<link rel="stylesheet" href="https://fonts.googleapis.com/css2?family=Noto+Sans:wght@400;600;700&family=Pinyon+Script&display=swap">
<style>
  :root {
    --page-bg: #ececec;
    --card-light: #f1efd2;
    --card-mid: #b8b8a3;
    --card-dark: #85867d;
    --card-corner: #4e4f4b;
    --cream: #f8f5c8;
    --cream-shade: #ece8b4;
    --ink: #1e1e1c;
  }
  html, body {
    margin: 0;
    padding: 0;
    width: 955px;
    height: 1200px;
    overflow: hidden;
    background: var(--page-bg);
  }
  .canvas {
    position: relative;
    width: 955px;
    height: 1200px;
  }
  .card {
    position: absolute;
    left: 82px;
    width: 791px;
    background:
      radial-gradient(ellipse 60% 70% at 62% 85%, var(--card-light) 0%, rgba(241,239,210,0) 60%),
      linear-gradient(135deg, var(--card-corner) 0%, var(--card-dark) 12%, var(--card-mid) 45%, #cfcdb4 75%, var(--card-mid) 100%);
    box-shadow: 0 6px 18px rgba(0,0,0,0.25);
  }
  .card--front { top: 116px; height: 450px; }
  .card--back {
    top: 634px; height: 457px;
    background:
      radial-gradient(ellipse 55% 65% at 22% 78%, var(--card-light) 0%, rgba(241,239,210,0) 60%),
      linear-gradient(225deg, var(--card-corner) 0%, var(--card-dark) 10%, var(--card-mid) 45%, #cfcdb4 70%, var(--card-mid) 100%);
  }
  .portrait-art {
    position: absolute;
    z-index: 1;
    background: linear-gradient(160deg, var(--cream) 0%, var(--cream-shade) 100%);
  }
  .portrait-art--front {
    left: 82px; top: 82px; width: 327px; height: 484px;
    clip-path: polygon(0% 7%, 30% 0%, 95% 5%, 100% 20%, 70% 45%, 45% 60%, 35% 100%, 0% 100%);
  }
  .portrait-art--back {
    left: 546px; top: 600px; width: 327px; height: 491px;
    clip-path: polygon(100% 7%, 70% 0%, 5% 5%, 0% 20%, 30% 45%, 55% 60%, 65% 100%, 100% 100%);
  }
  .contact, .brand-name, .strapline { z-index: 2; }
  .contact {
    position: absolute;
    left: 505px;
    top: 30px;
    margin: 0;
    font-family: "Noto Sans", Verdana, sans-serif;
    font-style: normal;
    font-size: 19px;
    line-height: 31px;
    color: var(--ink);
  }
  .contact__label { font-weight: 700; }
  .brand-name {
    position: absolute;
    margin: 0;
    font-family: "Noto Sans", Verdana, sans-serif;
    font-weight: 600;
    font-size: 36px;
    line-height: 1;
    letter-spacing: 2px;
    text-transform: uppercase;
    color: var(--ink);
    white-space: nowrap;
  }
  .card--front .brand-name { left: 109px; top: 318px; }
  .card--back .brand-name { left: 50px; top: 278px; }
  .strapline {
    position: absolute;
    left: 61px;
    top: 212px;
    margin: 0;
    font-family: "Pinyon Script", cursive;
    font-size: 36px;
    line-height: 1.2;
    color: var(--ink);
    white-space: nowrap;
  }
</style>
</head>
<body>
<main class="canvas">
  <section class="card card--front" aria-label="Card front">
    <address class="contact">
      www.plumeandcrest.example<br>
      info@plumeandcrest.example<br>
      <span class="contact__label">sales and enquiries</span><br>
      (44) 07500 418263
    </address>
    <p class="brand-name">Plume &amp; Crest</p>
  </section>
  <div class="portrait-art portrait-art--front" role="img" aria-label="Illustration of a woman in profile with long hair sweeping upward"></div>

  <section class="card card--back" aria-label="Card back">
    <p class="strapline">Luxury hair at every touch point !</p>
    <p class="brand-name">Plume &amp; Crest</p>
  </section>
  <div class="portrait-art portrait-art--back" role="img" aria-label="Illustration of a woman in profile with long hair sweeping upward, facing left"></div>
</main>
</body>
</html>
```